Marbeck Partners Exit Plan business consultant web site

This website is for a consulting business that helps other businesses with exit plans. Essentially, assists them with the sale of their business. This website should be very professional, almost with a wall street look. I would like a very attractive image on the homepage. Perhaps something that denotes success. Perhaps a picture of palm trees and a beach? I will leave it to you for interpretation.

Across the screen I would like the words "Does your business have an exit plan?"

Below that it should read the following:
Let us help you with a completely impartial, no obligation assessment (button with link to the contact page)

Also, please use logo in a prominent place on the website so it's easily seen.

Target Market(s)

Males 40+

Coding

Coded - Design and coding required

Number of Pages Required

5+ page

Colors

Designer to choose colors to be used in the design.

Requirements
Must have
• The tabs for the homepage on the top should be:
• 1. About us
• 2. Services
• 3. Industries
• 4. Our success
• 5. Contact
Nice to have
• Clean, professional image.
• Please put FB, Twitter, Linked In - logos at bottom.
• Here are two examples of a website to give you an idea:
• https://blog.trevanquill.com/library/why-every-business-owner-should-have-an-exit-plan
Should not have
• nothing whimsical or cartoon like

```html
<!DOCTYPE html>
<html lang="en">
<head>
<meta charset="utf-8">
<title>Marbeck Partners — Exit Planning Consultants</title>
<link rel="stylesheet" href="https://fonts.googleapis.com/css2?family=Arimo:wght@400;700&family=Montserrat:wght@400;600&display=swap">
<style>
:root{
  --ink:#111;
  --text:#333;
  --blue:#2196d3;
  --navy:#0b4a6e;
  --navy-deep:#083a58;
  --red:#d9342b;
  --red-dark:#b8231c;
  --grey-bg:#ebebeb;
  --card:#f4f4f4;
  --tile:#fafafa;
  --white:#fff;
}
*{margin:0;padding:0;box-sizing:border-box}
html,body{width:1200px;height:3830px;overflow:hidden}
body{position:relative;background:var(--white);font-family:"Arimo",Arial,sans-serif;color:var(--text)}

/* header */
.site-header{position:absolute;left:0;top:0;width:1200px;height:123px;background:var(--white)}
.brand{position:absolute;left:150px;top:7px;width:212px;display:flex;flex-direction:column;align-items:center;gap:9px}
.brand-square{width:62px;height:76px;background:var(--ink);border:3px solid var(--white);outline:2px solid var(--ink)}
.brand-name{font-size:23px;line-height:26px;color:var(--ink);letter-spacing:.5px;font-weight:400;white-space:nowrap}
.nav a{position:absolute;top:46px;font-size:14px;color:var(--ink);text-decoration:none}

/* hero */
.hero-photo{position:absolute;left:0;top:123px;width:1200px;height:613px;
  background:linear-gradient(100deg,#2b3642 0%,#55616c 28%,#6b7a5e 45%,#9aa2a8 62%,#c9cdd1 80%,#e4e6e8 100%);
  clip-path:polygon(0 0,1200px 0,1200px 308px,339px 609px,0 435px)}
.hero-band{position:absolute;left:0;top:0}
.hero-text{position:absolute;left:155px;top:222px;color:var(--white)}
.hero-text .light{font-size:36px;line-height:44px;font-weight:400}
.hero-text .bold{font-size:60px;line-height:58px;font-weight:700;letter-spacing:1px}
.hero-text .sub{font-size:25px;line-height:29px;margin-top:12px}
.btn{position:absolute;display:flex;align-items:center;justify-content:center;width:135px;height:49px;
  background:linear-gradient(#e2453b,var(--red-dark));color:var(--white);font-size:13px;font-weight:700;text-decoration:none;letter-spacing:.5px}

/* about */
.about-photo{position:absolute;border:2px solid #888;outline:1px solid #bbb;outline-offset:2px}
.about-line{position:absolute;left:503px;top:858px;width:157px;height:1px;background:#666}
.about-title{position:absolute;left:668px;top:848px;font-size:31px;font-weight:700;color:var(--blue)}
.about-copy{position:absolute;left:666px;top:892px;width:375px;font-size:14px;line-height:19.7px;color:var(--text)}

/* why choose */
.why{position:absolute;left:0;top:1298px;width:1200px;height:437px;
  background:linear-gradient(135deg,var(--navy-deep) 0%,var(--navy) 50%,#0a4466 100%)}
.section-title{position:absolute;left:0;width:1200px;text-align:center;font-weight:700;font-size:32px;color:var(--ink)}
.why .section-title{color:var(--white);top:90px;font-size:31px}
.why-icon{position:absolute;top:181px;width:56px;height:56px;background:var(--white);border:3px solid var(--white);outline:1px solid #9bb;display:flex;align-items:center;justify-content:center}
.why-head{position:absolute;top:181px;font-size:19px;line-height:23px;font-weight:400;color:var(--white);width:230px}
.why-body{position:absolute;top:241px;font-size:13px;line-height:19px;color:#d6e2ea;width:215px}

/* services */
.svc-divider-v{position:absolute;left:600px;top:1897px;width:1px;height:454px;background:#888}
.svc-divider-h{position:absolute;top:2123px;height:1px;background:#888}
.svc-mark{position:absolute;left:568px;top:2086px;width:64px;height:77px;background:var(--ink);border:3px solid var(--white);outline:2px solid var(--ink)}
.svc-icon{position:absolute;width:52px;height:52px}
.svc-title{position:absolute;font-size:20px;font-weight:400;color:var(--ink)}
.svc-body{position:absolute;font-size:13px;line-height:18px;color:var(--text);width:335px}

/* stories */
.stories{position:absolute;left:0;top:2412px;width:1200px;height:581px;background:var(--grey-bg)}
.quote-card{position:absolute;top:156px;width:433px;height:232px;background:var(--card);border:1px solid #ddd;
  display:flex;justify-content:center;padding:77px 48px 0;font-family:"Montserrat",sans-serif;font-size:13px;line-height:18px;text-align:center;color:#555}
.quote-tail{position:absolute;top:387px}
.avatar{position:absolute;top:421px;width:68px;height:68px;border-radius:50%}
.person{position:absolute;top:443px;font-family:"Montserrat",sans-serif;font-size:13px;line-height:19px;color:#333}
.person b{font-weight:600;color:var(--ink)}
.dot{position:absolute;top:2956px;width:9px;height:9px;border-radius:50%;background:var(--white)}

/* partners */
.partners{position:absolute;left:159px;top:3063px;width:883px;height:231px;background:#efefef}
.partner{position:absolute;width:152px;height:89px;background:var(--tile);border:1px solid #e2e2e2;display:flex;align-items:center;justify-content:center}
.partner span{display:block;width:78px;height:22px;background:#c9c9c9;border-radius:3px}

/* footer */
.site-footer{position:absolute;left:0;top:3349px;width:1200px;height:481px;background:var(--blue);color:var(--white)}
.foot-brand{position:absolute;left:150px;top:96px;width:212px;display:flex;flex-direction:column;align-items:center;gap:9px}
.foot-brand .brand-square{background:var(--blue);border-color:var(--white);outline-color:var(--white);width:64px;height:76px}
.foot-brand .brand-name{color:var(--white)}
.foot-about{position:absolute;left:159px;top:251px;width:290px;font-size:12.5px;line-height:18px}
.social{position:absolute;top:355px;width:37px;height:37px;border-radius:50%;background:var(--white)}
.newsletter{position:absolute;left:532px;top:98px;font-size:16px;line-height:22px;letter-spacing:.5px}
.news-input{position:absolute;left:691px;top:95px;width:352px;height:49px;background:var(--white);display:flex;align-items:center;padding-left:22px;color:#222;font-size:13px}
.news-send{position:absolute;right:12px;top:9px;width:32px;height:32px;border-radius:50%;background:var(--red)}
.foot-head{position:absolute;top:232px;font-size:17px;font-weight:400}
.contact-item{position:absolute;left:553px;font-size:12.5px;display:flex;align-items:center;gap:12px}
.svc-list{position:absolute;left:816px;top:270px;list-style:none;font-size:12.5px;line-height:22.5px}
.svc-list li::before{content:"";display:inline-block;width:5px;height:5px;border-radius:50%;background:var(--white);margin-right:11px;vertical-align:middle}
.copyright{position:absolute;left:0;top:432px;width:1200px;text-align:center;font-size:11px}
</style>
</head>
<body>

<header class="site-header">
  <div class="brand"><div class="brand-square"></div><div class="brand-name">Marbeck Partners</div></div>
  <nav class="nav">
    <a style="left:470px" href="#">Home</a>
    <a style="left:552px" href="#">About Us</a>
    <a style="left:657px" href="#">Services</a>
    <a style="left:755px" href="#">Industries</a>
    <a style="left:864px" href="#">Our success</a>
    <a style="left:989px" href="#">Contact</a>
  </nav>
</header>

<div class="hero-photo" role="img" aria-label="Photo of two businessmen shaking hands in front of an office building with colleagues behind"></div>
<svg class="hero-band" width="1200" height="760" viewBox="0 0 1200 760">
  <polygon points="532,672 1200,427 1200,436 534,680" fill="#2196d3"/>
</svg>

<div class="hero-text">
  <div class="light">Does your</div>
  <div class="bold">BUSINESS</div>
  <div class="light">Have an</div>
  <div class="bold">EXIT PLAN?</div>
  <div class="sub">Let us help you with a completely<br>impartial,no obligation assessment</div>
</div>
<a class="btn" style="left:158px;top:507px" href="#">CONTACT US</a>

<section>
  <div class="about-photo" style="left:159px;top:848px;width:344px;height:309px;background:linear-gradient(135deg,#6d6a66,#b9b4ad 55%,#e3e1dd)" role="img" aria-label="Photo of a team of consultants reviewing documents at a desk"></div>
  <div class="about-photo" style="left:459px;top:1013px;width:173px;height:219px;background:linear-gradient(160deg,#c9ccd0,#8d949b 60%,#5b6168)" role="img" aria-label="Photo of two colleagues discussing charts at a computer"></div>
  <div class="about-line"></div>
  <h2 class="about-title">ABOUT US</h2>
  <p class="about-copy">It is a long established fact that a reader will be distracted by the readable content of a page when looking at its layout. The point of using Lorem Ipsum is that it has a more-or-less normal distribution of<br>letters, as opposed to using 'Content here, content here', making it look like readable English.<br>Many desktop publishing packages and web page editors now use Lorem Ipsum as their</p>
  <a class="btn" style="left:668px;top:1062px" href="#">READ MORE</a>
</section>

<section class="why">
  <h2 class="section-title">WHY CHOOSE US?</h2>
  <div class="why-icon" style="left:158px"><svg width="34" height="34" viewBox="0 0 34 34" fill="none" stroke="#d9342b" stroke-width="2.5"><path d="M8 4v26M17 4v26M26 4v26"/><rect x="5" y="18" width="6" height="5" fill="#d9342b"/><rect x="14" y="9" width="6" height="5" fill="#d9342b"/><rect x="23" y="14" width="6" height="5" fill="#d9342b"/></svg></div>
  <h3 class="why-head" style="left:232px">Help you control when and how you exit.</h3>
  <p class="why-body" style="left:232px">It is a long established fact that a reader will be distracted by the readable content of a page when looking at its layout.</p>

  <div class="why-icon" style="left:473px"><svg width="34" height="34" viewBox="0 0 34 34" fill="none" stroke="#d9342b" stroke-width="2.5"><rect x="6" y="6" width="22" height="24" rx="2"/><path d="M11 13h12M11 19h12M11 25h7"/></svg></div>
  <h3 class="why-head" style="left:543px">Make you more financially prepared.</h3>
  <p class="why-body" style="left:543px">It is a long established fact that a reader will be distracted by the readable content of a page when looking at its layout.</p>

  <div class="why-icon" style="left:773px"><svg width="34" height="34" viewBox="0 0 34 34" fill="none" stroke="#d9342b" stroke-width="2.5"><path d="M4 8h26M8 4l-4 4 4 4M26 4l4 4-4 4"/><path d="M6 30V21l11-7 11 7v9z" fill="#d9342b"/></svg></div>
  <h3 class="why-head" style="left:840px">Clarify your transition choices.</h3>
  <p class="why-body" style="left:840px">It is a long established fact that a reader will be distracted by the readable content of a page when looking at its layout.</p>
</section>

<section>
  <h2 class="section-title" style="top:1817px">OUR SERVICES</h2>
  <div class="svc-divider-v"></div>
  <div class="svc-divider-h" style="left:373px;width:183px"></div>
  <div class="svc-divider-h" style="left:644px;width:183px"></div>
  <div class="svc-mark"></div>

  <svg class="svc-icon" style="left:156px;top:1941px" viewBox="0 0 52 52" fill="none" stroke="#d9342b" stroke-width="2"><circle cx="18" cy="9" r="6"/><path d="M8 40V24a10 10 0 0 1 20 0v16"/><circle cx="36" cy="38" r="7"/><circle cx="36" cy="38" r="2.5"/></svg>
  <h3 class="svc-title" style="left:244px;top:1940px">Strategy Consulting</h3>
  <p class="svc-body" style="left:244px;top:1974px">All the Lorem Ipsum generators on the Internet tend to repeat predefined chunks as necessary, making this the first true generator on the Internet. It uses a dictionary of over 200 Latin words, combined</p>

  <svg class="svc-icon" style="left:632px;top:1941px" viewBox="0 0 52 52" fill="none" stroke="#d9342b" stroke-width="2"><circle cx="15" cy="14" r="6"/><path d="M4 44V30a11 11 0 0 1 22 0v14"/><rect x="30" y="4" width="18" height="14" rx="2"/><path d="M34 9h10M34 13h7"/><rect x="30" y="32" width="18" height="12" rx="1"/></svg>
  <h3 class="svc-title" style="left:711px;top:1940px">Management Consulting</h3>
  <p class="svc-body" style="left:711px;top:1974px">All the Lorem Ipsum generators on the Internet tend to repeat predefined chunks as necessary, making this the first true generator on the Internet. It uses a dictionary of over 200 Latin words, combined</p>

  <svg class="svc-icon" style="left:156px;top:2185px" viewBox="0 0 64 52" width="64" fill="none" stroke="#d9342b" stroke-width="2"><path d="M14 38a10 10 0 0 1 0-20 14 14 0 0 1 27-4 11 11 0 0 1 9 24z"/><path d="M22 28l10-5 10 5-10 5z" fill="#d9342b"/></svg>
  <h3 class="svc-title" style="left:244px;top:2190px">Feasibility Study Services</h3>
  <p class="svc-body" style="left:244px;top:2224px">All the Lorem Ipsum generators on the Internet tend to repeat predefined chunks as necessary, making this the first true generator on the Internet. It uses a dictionary of over 200 Latin words, combined</p>

  <svg class="svc-icon" style="left:632px;top:2185px" viewBox="0 0 52 52" fill="none" stroke="#d9342b" stroke-width="2"><rect x="4" y="4" width="22" height="16" rx="2"/><path d="M26 12h20v16H36l-5 5v-5"/><circle cx="12" cy="32" r="4"/><path d="M4 48v-4a8 8 0 0 1 16 0v4"/><circle cx="36" cy="38" r="4"/><path d="M28 50v-3a8 8 0 0 1 16 0v3"/></svg>
  <h3 class="svc-title" style="left:711px;top:2190px">Business Plan Consulting Services</h3>
  <p class="svc-body" style="left:711px;top:2224px">All the Lorem Ipsum generators on the Internet tend to repeat predefined chunks as necessary, making this the first true generator on the Internet. It uses a dictionary of over 200 Latin words, combined</p>
</section>

<section class="stories">
  <h2 class="section-title" style="top:90px">OUR SUCCESS STORIES</h2>
  <div class="quote-card" style="left:159px"><p>Ledgerline is worth much more than I paid. The very best. Just what I was looking for. It really saves me time and effort.<br>Ledgerline is exactly what our business has been lacking.</p></div>
  <svg class="quote-tail" style="left:208px" width="40" height="24"><polygon points="0,0 36,0 4,22" fill="#f4f4f4"/></svg>
  <div class="avatar" style="left:174px;background:radial-gradient(circle at 50% 40%,#c89a80,#f0b0a8)" role="img" aria-label="Portrait of Owen Harrow"></div>
  <div class="person" style="left:259px"><b>Owen Harrow</b><br>Launchwell</div>

  <div class="quote-card" style="left:610px"><p>I use Ledgerline often. It really saves me time and effort. Ledgerline is exactly what our business has been lacking. Dude, your stuff is the bomb!</p></div>
  <svg class="quote-tail" style="left:659px" width="40" height="24"><polygon points="0,0 36,0 4,22" fill="#f4f4f4"/></svg>
  <div class="avatar" style="left:625px;background:radial-gradient(circle at 50% 40%,#9a7a62,#6e7a80)" role="img" aria-label="Portrait of Desmond Kael"></div>
  <div class="person" style="left:708px"><b>Desmond Kael</b><br>Trademoor</div>
</section>
<span class="dot" style="left:574px"></span>
<span class="dot" style="left:595px;background:var(--blue)"></span>
<span class="dot" style="left:615px"></span>

<section class="partners" aria-label="Partner badges">
  <div class="partner" style="left:21px;top:17px"><span></span></div>
  <div class="partner" style="left:196px;top:17px"><span></span></div>
  <div class="partner" style="left:372px;top:17px"><span></span></div>
  <div class="partner" style="left:547px;top:17px"><span></span></div>
  <div class="partner" style="left:723px;top:17px"><span></span></div>
  <div class="partner" style="left:21px;top:128px"><span></span></div>
  <div class="partner" style="left:196px;top:128px"><span></span></div>
  <div class="partner" style="left:372px;top:128px"><span></span></div>
  <div class="partner" style="left:547px;top:128px"><span></span></div>
  <div class="partner" style="left:723px;top:128px"><span></span></div>
</section>

<footer class="site-footer">
  <div class="foot-brand"><div class="brand-square"></div><div class="brand-name">Marbeck Partners</div></div>
  <p class="foot-about">All the Lorem Ipsum generators on the Internet tend to repeat predefined chunks as necessary, making this the first true generator on the Internet. . .</p>
  <a class="social" style="left:158px" href="#" aria-label="Social profile 1"></a>
  <a class="social" style="left:201px" href="#" aria-label="Social profile 2"></a>
  <a class="social" style="left:245px" href="#" aria-label="Social profile 3"></a>

  <div class="newsletter">NEWSLETTER<br>SUBSCRIBE NOW</div>
  <div class="news-input">Enter your mail ID
    <div class="news-send"><svg width="32" height="32" viewBox="0 0 32 32"><path d="M9 17l14-7-5 14-3-5z" fill="#fff"/></svg></div>
  </div>

  <h4 class="foot-head" style="left:547px">Quick Contact</h4>
  <div class="contact-item" style="top:271px"><svg width="12" height="14" viewBox="0 0 12 14"><path d="M6 0a5 5 0 0 1 5 5c0 4-5 9-5 9S1 9 1 5a5 5 0 0 1 5-5z" fill="#fff"/><circle cx="6" cy="5" r="2" fill="#2196d3"/></svg>lorem Ipsum,1234</div>
  <div class="contact-item" style="top:303px"><svg width="12" height="12" viewBox="0 0 12 12"><path d="M2 1l3 0 1 3-2 1a7 7 0 0 0 3 3l1-2 3 1v3c-6 0-10-4-10-9z" fill="#fff"/></svg>1234-456-789</div>
  <div class="contact-item" style="top:335px"><svg width="12" height="10" viewBox="0 0 12 10"><rect width="12" height="10" rx="1" fill="#fff"/><path d="M0 1l6 5 6-5" stroke="#2196d3" fill="none"/></svg>marbeckpartners@mail.com</div>

  <h4 class="foot-head" style="left:816px">Our Services</h4>
  <ul class="svc-list">
    <li>Strategy Consulting</li>
    <li>Management Consulting</li>
    <li>Feasibility Study Services</li>
    <li>Business Plan Consulting Services</li>
  </ul>

  <div class="copyright">Copyright©2020 marbeckpartners.com. All Rights Reserved.</div>
</footer>

</body>
</html>
```